Bref créative
Larkfield Joint & Motion Medicine
Letterhead, stationary and card design
Professional
Dr. Paul Korvitz
Director
418 West 71st Street
New York, NY 10187
director@larkfieldjoint.com
larkfieldjoint.com
Here is the logo file for use with the project

```html
<!DOCTYPE html>
<html lang="en">
<head>
<meta charset="utf-8">
<title>Larkfield Joint &amp; Motion Medicine — Stationery</title>
<link href="https://fonts.googleapis.com/css2?family=Montserrat:wght@500;600&family=Open+Sans:wght@400;600&display=swap" rel="stylesheet">
<style>
  :root{
    --navy:#2f2a66;
    --gold:#c8832c;
    --ink:#6b6c70;
    --paper:#ffffff;
    --backdrop:#e6e6ea;
    --rule:#d6d6dc;
  }
  *{box-sizing:border-box;margin:0;padding:0}
  html,body{width:1200px;height:854px;overflow:hidden}
  body{background:var(--backdrop);font-family:"Open Sans",Arial,sans-serif;color:var(--ink)}
  .canvas{position:relative;width:1200px;height:854px;overflow:hidden}

  .sheet{position:absolute;background:var(--paper);box-shadow:0 2px 8px rgba(0,0,0,.12)}

  /* brand lockup */
  .brand{display:flex;align-items:center;gap:10px}
  .brand-dot{flex:none;border-radius:50%;background:var(--gold)}
  .brand-name{font-family:"Montserrat",Arial,sans-serif;font-weight:500;color:var(--navy);text-transform:uppercase;line-height:1.12;letter-spacing:.02em}

  /* letterhead */
  .letterhead{left:420px;top:30px;width:560px;height:794px;padding:44px 48px 0}
  .letterhead .brand-dot{width:44px;height:44px}
  .letterhead .brand-name{font-size:15px}
  .letter{margin-top:40px;font-size:9.5px;line-height:1.55}
  .letter .recipient{margin-bottom:18px}
  .letter .salutation{margin-bottom:14px}
  .letter p{margin-bottom:12px}
  .letter .closing{margin-top:22px}
  .signature{display:block;width:110px;height:34px;margin:8px 0 6px;border-radius:4px;background:linear-gradient(90deg,#efeff2,#e3e3e8)}
  .letter-footer{position:absolute;left:48px;right:48px;bottom:30px;border-top:1.5px solid var(--navy);padding-top:7px;font-size:8px;color:var(--ink)}
  .letter-footer b{color:var(--gold);font-weight:600}

  /* envelope back */
  .envelope-back{left:40px;top:60px;width:360px;height:200px}
  .envelope-back svg{display:block}

  /* envelope front */
  .envelope-front{left:40px;top:470px;width:360px;height:170px;padding:22px 22px 0;overflow:hidden}
  .envelope-front .brand-dot{width:30px;height:30px}
  .envelope-front .brand-name{font-size:10.5px}
  .envelope-front .address{margin-top:8px;font-size:7px;color:var(--gold)}
  .envelope-front .band{position:absolute;left:0;right:0;bottom:0;height:14px;background:var(--navy)}

  /* business card */
  .business-card{left:1000px;top:210px;width:180px;height:104px;padding:12px 12px 0;overflow:hidden}
  .business-card .brand{gap:6px}
  .business-card .brand-dot{width:18px;height:18px}
  .business-card .brand-name{font-size:6.5px}
  .card-details{position:absolute;right:12px;top:44px;text-align:right;font-size:6px;line-height:1.5}
  .card-details .person{color:var(--gold);font-weight:600;font-size:7px}
  .business-card .band{position:absolute;left:0;right:0;bottom:0;height:7px;background:var(--navy)}

  /* compliment slip */
  .compliment-slip{left:1000px;top:350px;width:180px;height:70px;overflow:hidden}
  .compliment-slip .brand-dot{position:absolute;right:14px;top:14px;width:24px;height:24px}
  .compliment-slip .band{position:absolute;left:0;right:0;bottom:0;height:9px;background:var(--navy)}
</style>
</head>
<body>
<main class="canvas">

  <section class="sheet envelope-back" aria-label="Envelope back">
    <svg width="360" height="200" viewBox="0 0 360 200">
      <rect width="360" height="200" fill="var(--paper)"/>
      <path d="M0 0H360V46C300 46 220 58 180 92C140 58 60 46 0 46Z" fill="var(--navy)"/>
      <path d="M0 46C60 46 140 58 180 92C220 58 300 46 360 46" fill="none" stroke="var(--rule)" stroke-width="1"/>
      <path d="M0 200L150 118M360 200L210 118" stroke="var(--rule)" stroke-width="1"/>
      <circle cx="180" cy="30" r="11" fill="var(--gold)"/>
      <circle cx="180" cy="132" r="13" fill="var(--gold)"/>
    </svg>
  </section>

  <section class="sheet envelope-front" aria-label="Envelope front">
    <div class="brand">
      <span class="brand-dot"></span>
      <span class="brand-name">Larkfield<br>Joint &amp; Motion<br>Medicine</span>
    </div>
    <p class="address">418 West 71st Street New York, NY 10187</p>
    <div class="band"></div>
  </section>

  <article class="sheet letterhead" aria-label="Letterhead">
    <header class="brand">
      <span class="brand-dot"></span>
      <span class="brand-name">Larkfield<br>Joint &amp; Motion<br>Medicine</span>
    </header>
    <div class="letter">
      <p class="recipient">Someone Somebody<br>100 Long St<br>Brisbane, Australia</p>
      <p class="salutation">Dear Someone Somebody,</p>
      <p>Lorem ipsum dolor sit amet, consectetuer adipiscing elit, sed diam nonummy nibh euismod tincidunt ut laoreet dolore magna aliquam erat volutpat. Ut wisi enim ad minim veniam, quis nostrud exerci tation ullamcorper suscipit lobortis nisl ut aliquip ex ea commodo consequat. Duis autem vel eum iriure dolor in hendrerit in vulputate velit esse molestie consequat, vel illum dolore eu feugiat nulla facilisis at vero eros et accumsan et iusto odio dignissim qui blandit praesent luptatum zzril delenit augue duis dolore te feugait nulla facilisi.</p>
      <p>Lorem ipsum dolor sit amet, consectetuer adipiscing elit, sed diam nonummy nibh euismod tincidunt ut laoreet dolore magna aliquam erat volutpat. Ut wisi enim ad minim veniam, quis nostrud exerci tation ullamcorper suscipit lobortis nisl ut aliquip ex ea commodo consequat. Duis autem vel eum iriure dolor in hendrerit in vulputate velit esse molestie consequat, vel illum dolore eu feugiat nulla facilisis.</p>
      <p>Lorem ipsum dolor sit amet, consectetuer adipiscing elit, sed diam nonummy nibh euismod tincidunt ut laoreet dolore magna aliquam erat volutpat. Ut wisi enim ad minim veniam, quis nostrud exerci tation ullamcorper suscipit lobortis nisl ut aliquip ex ea commodo consequat. Duis autem vel eum iriure dolor in hendrerit in vulputate velit esse molestie consequat, vel illum dolore eu feugiat nulla facilisis at vero eros et accumsan et iusto odio dignissim qui blandit praesent luptatum zzril delenit augue duis dolore te feugait nulla facilisi.</p>
      <p class="closing">Your Sincerely,<br>Martin Hale</p>
      <span class="signature" role="img" aria-label="Handwritten signature"></span>
    </div>
    <footer class="letter-footer">418 West 71st Street New York, NY 10187 | <b>Phone:</b> 212-555-0148 | <b>Fax:</b> 212-555-0163 | www.larkfieldjoint.com</footer>
  </article>

  <section class="sheet business-card" aria-label="Business card">
    <div class="brand">
      <span class="brand-dot"></span>
      <span class="brand-name">Larkfield<br>Joint &amp; Motion<br>Medicine</span>
    </div>
    <div class="card-details">
      <p class="person">Dr. Paul Korvitz</p>
      <p>Director</p>
      <p>418 West 71st Street, New York, NY 10187</p>
      <p>Phone 212-555-0148</p>
      <p>director@larkfieldjoint.com</p>
    </div>
    <div class="band"></div>
  </section>

  <section class="sheet compliment-slip" aria-label="Compliment slip">
    <span class="brand-dot"></span>
    <div class="band"></div>
  </section>

</main>
</body>
</html>
```